Domain Parking page and Listing page

1)
In need a design of a domain parking page, mainly with the same features as VORIQ.com as can be seen here: https://wanderplum.com/

2)
I need a design of a website with all domains listed. There's no company logo/name yet so it should be in plain font, for example "tilmorex.site" (this is just an example), similar as:
https://voriq.com/search?&terms=park&results=50&order_by=relevance

Delivery after approval in HTML/CSS. Should be responsive. Ideally use a framework like Bootstrap

Target Market(s)

Domain buyers, business owners

Industry/Entity Type

Business to business, Marketing, domains

Coding

Coded - Design and coding required

Number of Pages Required

2 page

Font styles to use
Sans Serif

Requirements
Must have
• Responsive design, worldly design.

```html
<!DOCTYPE html>
<html lang="en">
<head>
<meta charset="utf-8">
<title>quenlark.host is for sale | VORIQ.com</title>
<link rel="stylesheet" href="https://fonts.googleapis.com/css2?family=Roboto:wght@400;500;700&family=Lato:wght@400;700&display=swap">
<style>
:root{
  --navy:#0b2a64;
  --navy-deep:#06173f;
  --royal:#0f3c8c;
  --ink:#0c1a33;
  --text:#4b4f58;
  --muted:#6d717a;
  --green:#22b36b;
  --white:#ffffff;
  --card-shadow:0 10px 30px rgba(20,40,90,.08);
  --footer:#3d3d3f;
}
*{box-sizing:border-box;margin:0;padding:0}
html,body{width:1200px;height:2473px;overflow:hidden}
body{position:relative;background:var(--white);font-family:"Roboto",sans-serif;color:var(--ink)}
.abs{position:absolute}
.hero-bg{position:absolute;left:0;top:0;width:1200px;height:790px}
.brand{position:absolute;display:flex;align-items:center;gap:14px;font-family:"Roboto",sans-serif;font-weight:500;color:var(--white)}
.brand-mark{background:var(--white);border-radius:12px}
.topbar .brand{left:111px;top:47px;font-size:36px}
.topbar .brand-mark{width:52px;height:52px}
.nav{position:absolute;top:62px;right:111px;display:flex;gap:39px;font-family:"Lato",sans-serif;font-size:15px;color:var(--white)}
.nav a{color:inherit;text-decoration:none}
.eyebrow{left:111px;top:238px;font-size:22px;color:var(--white)}
.domain-title{left:110px;top:276px;font-size:49px;font-weight:700;color:var(--white)}
.sale{left:111px;top:343px;font-size:22px;color:var(--white)}
.avatar{left:111px;top:403px;width:89px;height:82px;border-radius:16px;background:linear-gradient(160deg,#f2e7da,#d9a777)}
.listed{left:225px;top:418px;font-size:16px;color:#dfe6f5}
.seller{left:225px;top:445px;font-size:20px;font-weight:500;color:var(--white)}
.offer-card{left:600px;top:148px;width:490px;height:489px;background:#fff;border-radius:46px;box-shadow:0 20px 50px rgba(0,0,0,.15)}
.offer-card h2{position:absolute;top:62px;width:100%;text-align:center;font-size:44px;font-weight:700;color:var(--navy-deep)}
.offer-field{position:absolute;left:54px;top:138px;width:383px;height:64px;border:1px solid #9aa3b5;border-radius:6px;display:flex;align-items:center;padding-left:28px;font-size:16px;color:#3b3f47}
.offer-go{position:absolute;right:6px;top:7px;width:58px;height:49px;border-radius:4px;background:linear-gradient(180deg,var(--royal),var(--navy-deep));display:flex;align-items:center;justify-content:center}
.perks{position:absolute;left:82px;top:228px;list-style:none;font-size:16px;color:#333}
.perks li{display:flex;align-items:center;gap:11px;height:39px}
.perks em{font-style:normal;color:var(--green)}
.pay-row{position:absolute;display:flex}
.pay-row span{display:block;background:#fff;border:1.5px solid #c9ccd2;border-radius:3px}
.offer-card .pay-row{left:53px;top:372px;gap:12px}
.offer-card .pay-row span{width:68px;height:45px}
.section-title{left:111px;top:752px;font-size:40px;font-weight:700;line-height:56px;color:var(--ink)}
.section-lead{left:111px;top:886px;font-size:16px;color:var(--text)}
.pill{position:absolute;display:flex;align-items:center;justify-content:center;border-radius:24px;background:linear-gradient(180deg,var(--royal),var(--navy-deep));color:#fff;font-weight:700;font-size:16px}
.how{left:884px;top:863px;width:205px;height:42px}
.bg-swoosh{left:880px;top:960px;width:420px;height:430px;border-radius:50%;background:#f3f5f8}
.feature{position:absolute;top:963px;width:308px;height:352px;background:#fff;border-radius:22px;box-shadow:var(--card-shadow);overflow:hidden}
.feature svg.icon{position:absolute;left:30px;top:48px}
.feature h3{position:absolute;left:31px;top:140px;font-size:22px;font-weight:700;line-height:32px;color:var(--ink)}
.feature p{position:absolute;left:31px;top:218px;width:260px;font-size:13.5px;line-height:23.4px;color:var(--muted)}
.feature .corner{position:absolute;right:0;bottom:0;width:60px;height:56px;border-top-left-radius:40px;background:linear-gradient(180deg,var(--royal),var(--navy-deep));display:flex;align-items:center;justify-content:center}
.explore-title{left:0;top:1442px;width:1200px;text-align:center;font-size:40px;font-weight:700;color:var(--ink)}
.domain-card{position:absolute;top:1537px;width:233px;height:223px;background:#fff;border-radius:18px;box-shadow:var(--card-shadow)}
.domain-card .head{height:66px;border-radius:18px 18px 30px 30px;background:var(--royal);color:#fff;font-size:24px;font-weight:500;display:flex;align-items:center;justify-content:center}
.domain-card .price{position:absolute;top:90px;width:100%;text-align:center;font-size:27px;font-weight:700;color:var(--royal)}
.outline-btn{position:absolute;top:146px;left:50%;transform:translateX(-50%);height:33px;border:2px solid var(--royal);border-radius:18px;color:var(--royal);font-weight:700;font-size:16px;display:flex;align-items:center;justify-content:center}
.round{position:absolute;top:1820px;width:50px;height:50px;border-radius:50%;background:var(--royal);display:flex;align-items:center;justify-content:center}
.more{left:581px;top:1823px;width:205px;height:43px}
.footer-bg{position:absolute;left:0;top:0;width:1200px;height:2473px}
.chat{left:947px;top:1895px;width:86px;height:85px;background:#fff;border-radius:14px;box-shadow:0 8px 22px rgba(0,0,0,.12);display:flex;align-items:center;justify-content:center}
.site-footer .brand{left:0;width:1200px;justify-content:center;top:2108px;font-size:38px}
.site-footer .brand-mark{width:54px;height:54px}
.foot-nav{position:absolute;left:0;width:1200px;display:flex;justify-content:center;font-family:"Lato",sans-serif;font-size:15px;color:#f0f0f0}
.foot-nav.main{top:2192px;gap:39px}
.foot-nav.legal{top:2244px;gap:60px}
.social{position:absolute;top:2296px;left:0;width:1200px;display:flex;justify-content:center;gap:7px}
.social span{width:34px;height:34px;border-radius:50%;background:var(--royal)}
.copy{left:0;top:2355px;width:1200px;text-align:center;font-family:"Lato",sans-serif;font-size:13px;color:#eee}
.site-footer .pay-row{left:0;width:1200px;justify-content:center;top:2402px;gap:8px}
.site-footer .pay-row span{width:50px;height:33px}
</style>
</head>
<body>

<header class="hero">
  <svg class="hero-bg" viewBox="0 0 1200 790" aria-hidden="true">
    <defs>
      <linearGradient id="heroGrad" x1="0" y1="0" x2="0" y2="1">
        <stop offset="0" stop-color="#0d3a86"/>
        <stop offset="1" stop-color="#051538"/>
      </linearGradient>
    </defs>
    <path d="M0 0H1200V715C1130 770 1000 782 870 768C650 742 430 600 250 595C140 592 60 610 0 630Z" fill="url(#heroGrad)"/>
  </svg>

  <div class="topbar">
    <div class="brand"><span class="brand-mark"></span>VORIQ.com</div>
    <nav class="nav">
      <a href="#">A Nestara Brand</a><a href="#">Buy a domain</a><a href="#">Sell your domain</a><a href="#">Learn</a><a href="#">Company</a>
    </nav>
  </div>

  <p class="abs eyebrow">The Domain Name</p>
  <h1 class="abs domain-title">quenlark.host</h1>
  <p class="abs sale">is for sale!</p>
  <div class="abs avatar" role="img" aria-label="Seller avatar illustration"></div>
  <p class="abs listed">Listed by</p>
  <p class="abs seller">Lumavent</p>

  <section class="abs offer-card">
    <h2>Make An Offer</h2>
    <div class="offer-field">My Offer In USD
      <span class="offer-go"><svg width="26" height="14" viewBox="0 0 26 14"><path d="M1 7H24M18 1L24 7L18 13" stroke="#fff" stroke-width="1.8" fill="none"/></svg></span>
    </div>
    <ul class="perks">
      <li><svg width="20" height="20" viewBox="0 0 20 20"><circle cx="10" cy="10" r="8.5" stroke="#22b36b" stroke-width="1.6" fill="none"/><path d="M6 10l3 3 5-6" stroke="#22b36b" stroke-width="1.8" fill="none"/></svg><span><em>Free</em> Ownership transfer</span></li>
      <li><svg width="20" height="20" viewBox="0 0 20 20"><circle cx="10" cy="10" r="8.5" stroke="#22b36b" stroke-width="1.6" fill="none"/><path d="M6 10l3 3 5-6" stroke="#22b36b" stroke-width="1.8" fill="none"/></svg><span><em>Free</em> Transaction support</span></li>
      <li><svg width="20" height="20" viewBox="0 0 20 20"><circle cx="10" cy="10" r="8.5" stroke="#22b36b" stroke-width="1.6" fill="none"/><path d="M6 10l3 3 5-6" stroke="#22b36b" stroke-width="1.8" fill="none"/></svg><span>Secure payments</span></li>
    </ul>
    <div class="pay-row" aria-label="Accepted payment methods"><span></span><span></span><span></span><span></span><span></span></div>
  </section>
</header>

<main>
  <h2 class="abs section-title">The Simple, Safe Way To<br>Buy Domain Names</h2>
  <p class="abs section-lead">No matter what kind of domain you want to buy, we make the transfer simple and safe.</p>
  <a class="pill how">Here’s How It Works</a>

  <div class="abs bg-swoosh" aria-hidden="true"></div>

  <article class="feature" style="left:111px">
    <svg class="icon" width="80" height="80" viewBox="0 0 80 80"><path d="M40 8L64 17V38C64 54 53 64 40 70C27 64 16 54 16 38V17Z" fill="#4f7df0"/><circle cx="40" cy="39" r="13" fill="#0c1a33"/><path d="M33 39l5 5 9-10" stroke="#fff" stroke-width="3" fill="none"/></svg>
    <h3>Buyer Protection<br>Program</h3>
    <p>Lorem ipsum dolor sit amet, consectetur adipiscing elit, sed do eiusmod tempor incididunt ut labore et dolore magna aliqua. Quis ipsum suspendisse</p>
    <span class="corner"><svg width="22" height="12" viewBox="0 0 22 12"><path d="M1 6H20M15 1L20 6L15 11" stroke="#fff" stroke-width="1.6" fill="none"/></svg></span>
  </article>
  <article class="feature" style="left:446px">
    <svg class="icon" width="80" height="80" viewBox="0 0 80 80"><path d="M6 30L76 14L36 68L30 46Z" fill="none" stroke="#1a2a4a" stroke-width="2"/><path d="M30 46L76 14L22 40Z" fill="#6a7ef0"/></svg>
    <h3>Fast And Easy<br>Transfers</h3>
    <p>Lorem ipsum dolor sit amet, consectetur adipiscing elit, sed do eiusmod tempor incididunt ut labore et dolore magna aliqua. Quis ipsum suspendisse</p>
    <span class="corner"><svg width="22" height="12" viewBox="0 0 22 12"><path d="M1 6H20M15 1L20 6L15 11" stroke="#fff" stroke-width="1.6" fill="none"/></svg></span>
  </article>
  <article class="feature" style="left:781px">
    <svg class="icon" width="80" height="80" viewBox="0 0 80 80"><rect x="6" y="20" width="56" height="36" rx="6" fill="#0c1a33"/><rect x="12" y="30" width="14" height="8" rx="4" fill="#fff"/><rect x="22" y="38" width="34" height="34" rx="10" fill="#5a7df0"/></svg>
    <h3>Hassle Free<br>Payments</h3>
    <p>Lorem ipsum dolor sit amet, consectetur adipiscing elit, sed do eiusmod tempor incididunt ut labore et dolore magna aliqua. Quis ipsum suspendisse</p>
    <span class="corner"><svg width="22" height="12" viewBox="0 0 22 12"><path d="M1 6H20M15 1L20 6L15 11" stroke="#fff" stroke-width="1.6" fill="none"/></svg></span>
  </article>

  <h2 class="abs explore-title">Explore other popular domains from the seller</h2>

  <div class="domain-card" style="left:85px"><div class="head">zelbo.com</div><p class="price">$ 8,590</p><a class="outline-btn" style="width:103px">Buy</a></div>
  <div class="domain-card" style="left:351px"><div class="head">fenu.com</div><p class="price">$ 69,900</p><a class="outline-btn" style="width:103px">Buy</a></div>
  <div class="domain-card" style="left:616px"><div class="head">kovra.com</div><a class="outline-btn" style="width:129px">Make Offer</a></div>
  <div class="domain-card" style="left:882px"><div class="head">tamix.com</div><a class="outline-btn" style="width:129px">Make Offer</a></div>

  <a class="round" style="left:414px"><svg width="18" height="12" viewBox="0 0 18 12"><path d="M17 6H2M7 1L2 6L7 11" stroke="#fff" stroke-width="1.6" fill="none"/></svg></a>
  <a class="round" style="left:474px"><svg width="18" height="12" viewBox="0 0 18 12"><path d="M1 6H16M11 1L16 6L11 11" stroke="#fff" stroke-width="1.6" fill="none"/></svg></a>
  <a class="pill more">See More Domains</a>
</main>

<footer class="site-footer">
  <svg class="footer-bg" viewBox="0 0 1200 2473" aria-hidden="true">
    <path d="M0 1818C90 1990 260 2072 460 2070C700 2066 850 1930 1000 1935C1100 1940 1170 2000 1200 2018V2473H0Z" fill="var(--footer)"/>
  </svg>
  <div class="abs chat"><svg width="42" height="38" viewBox="0 0 42 38"><circle cx="26" cy="14" r="12" fill="#4f7df0"/><ellipse cx="17" cy="23" rx="15" ry="12" fill="#0f3c8c"/><circle cx="11" cy="23" r="2" fill="#fff"/><circle cx="17" cy="23" r="2" fill="#fff"/><circle cx="23" cy="23" r="2" fill="#fff"/></svg></div>
  <div class="brand"><span class="brand-mark"></span>VORIQ.com</div>
  <nav class="foot-nav main"><span>A Nestara Brand</span><span>Buy a domain</span><span>Sell your domain</span><span>Learn</span><span>Company</span></nav>
  <nav class="foot-nav legal"><span>Terms Of Service</span><span>|</span><span>Privacy Policy</span><span>|</span><span>Support</span></nav>
  <div class="social" aria-label="Social links"><span></span><span></span><span></span></div>
  <p class="abs copy">© Copyright 2023 | All Rights Reserved</p>
  <div class="pay-row" aria-label="Accepted payment methods"><span></span><span></span><span></span><span></span><span></span></div>
</footer>

</body>
</html>
```